Building Servicess

We need a new business card design for a company. We specialise in: Electrical/Site temporary electrics, Data/Network Installation, Passive Fire Protection

Industry/Entity Type

Construction

Contact Information for Business Card

Services provided as detailed on project description

Font styles to use
Serif

Colors
0054AA
0677BA
7BADD7
CADEEF
E8F1F8
00AB8E
00BBA5
67D7C9
C6EFE9
E9F9F6
EB3D1F
EC4F4E
F09395
F8D3D4
FCEDEE

Requirements
Must have
• Company logo-contact details-phone numbers

```html
<!DOCTYPE html>
<html lang="en">
<head>
<meta charset="utf-8">
<title>Norvale Build Services – Business Card</title>
<link href="https://fonts.googleapis.com/css2?family=Noto+Serif:wght@400;700&display=swap" rel="stylesheet">
<style>
  :root {
    --blue: #2586fd;
    --grey: #798c8d;
    --paper: #f4f8f9;
    --ink: #333333;
    --page: #ffffff;
  }
  html, body {
    margin: 0;
    width: 1200px;
    height: 1003px;
    overflow: hidden;
    background: var(--page);
    font-family: "Noto Serif", Georgia, serif;
  }
  .canvas { position: relative; width: 1200px; height: 1003px; }
  .card {
    position: absolute;
    left: 284px;
    width: 632px;
    height: 360px;
    background: var(--paper);
    overflow: hidden;
  }
  .card--front { top: 102px; }
  .card--back { top: 541px; }
  .card__shapes { position: absolute; inset: 0; width: 632px; height: 360px; }
  .shape--blue { fill: var(--blue); }
  .shape--grey { fill: var(--grey); }

  .holder-name {
    position: absolute; left: 80px; top: 22px; margin: 0;
    font-size: 31px; font-weight: 700; color: var(--blue);
    letter-spacing: 0.2px; line-height: 1;
  }
  .holder-role {
    position: absolute; left: 80px; top: 62px; margin: 0;
    font-size: 19px; font-weight: 700; color: var(--ink); line-height: 1;
  }
  .contact {
    position: absolute; left: 80px; top: 104px;
    display: flex; align-items: center; gap: 15px;
  }
  .contact__icon {
    width: 35px; height: 35px; border-radius: 4px; background: var(--blue);
    display: flex; align-items: center; justify-content: center;
  }
  .contact__lines { font-size: 17px; color: var(--ink); line-height: 22px; }

  .brand-name {
    position: absolute; display: flex; align-items: center;
    color: var(--blue); font-weight: 700; text-transform: uppercase; white-space: nowrap;
  }
  .brand-name__mark { background: var(--blue); flex: none; }
  .card--front .brand-name {
    left: 98px; top: 200px; font-size: 19px; line-height: 1.25; gap: 12px;
  }
  .card--front .brand-name__mark { width: 40px; height: 40px; }
  .card--back .brand-name {
    left: 0; right: 0; top: 150px; justify-content: center;
    font-size: 36px; gap: 16px;
  }
  .card--back .brand-name__mark { width: 40px; height: 40px; }
</style>
</head>
<body>
<div class="canvas">

  <section class="card card--front">
    <svg class="card__shapes" viewBox="0 0 1106 631" preserveAspectRatio="none" aria-hidden="true">
      <polygon class="shape--blue" points="0,0 97,0 97,550 757,550 831,631 0,631"/>
      <polygon class="shape--grey" points="878,0 1042,0 781,331 1057,631 882,631 614,337"/>
      <polygon class="shape--blue" points="1106,10 1106,217 1015,331 1106,428 1106,618 848,337"/>
    </svg>

    <h1 class="holder-name">MAREK WOLANSKI</h1>
    <p class="holder-role">MANAGING DIRECTOR</p>

    <div class="contact">
      <div class="contact__icon">
        <svg width="22" height="22" viewBox="0 0 24 24" aria-hidden="true">
          <path fill="#ffffff" d="M6.6 10.8c1.4 2.8 3.8 5.1 6.6 6.6l2.2-2.2c.3-.3.7-.4 1-.2 1.1.4 2.3.6 3.6.6.6 0 1 .4 1 1V20c0 .6-.4 1-1 1C10.6 21 3 13.4 3 4c0-.6.4-1 1-1h3.5c.6 0 1 .4 1 1 0 1.3.2 2.5.6 3.6.1.3 0 .7-.2 1l-2.3 2.2z"/>
        </svg>
      </div>
      <div class="contact__lines">
        <div>Office &nbsp;&nbsp;: 020 4150 2398</div>
        <div>Mobile : 075 0312 8841</div>
      </div>
    </div>

    <div class="brand-name">
      <span class="brand-name__mark"></span>
      <span>Norvale Build<br>Services Ltd</span>
    </div>
  </section>

  <section class="card card--back">
    <svg class="card__shapes" viewBox="0 0 1106 631" preserveAspectRatio="none" aria-hidden="true">
      <polygon class="shape--grey" points="27,0 89,0 13,96 0,96 0,34"/>
      <polygon class="shape--blue" points="116,0 179,0 104,96 41,96"/>
      <polygon class="shape--grey" points="213,0 275,0 200,96 137,96"/>
      <polygon class="shape--blue" points="303,0 1106,0 1106,96 227,96"/>
      <polygon class="shape--blue" points="0,535 773,535 848,631 0,631"/>
      <polygon class="shape--grey" points="800,535 863,535 938,631 874,631"/>
      <polygon class="shape--blue" points="896,535 958,535 1034,631 971,631"/>
      <polygon class="shape--grey" points="985,535 1048,535 1106,609 1106,631 1061,631"/>
      <polygon class="shape--blue" points="1087,535 1106,535 1106,559"/>
    </svg>

    <div class="brand-name">
      <span class="brand-name__mark"></span>
      <span>Norvale Build Services</span>
    </div>
  </section>

</div>
</body>
</html>
```